Business card for Full Stable Works Vanhoorne

I would like to have me designed an professional business card with my existing logo for my company called : full stable works vanhoorne gcv.
I prefer a two sided business card with on the back side only the horses head and the website : fswvanhoorne-example.eu
Only one colour shouldbe all right.
The logo must appear in a nic professional way on the business card.

Other suggestion are welcome.

All copy wrights must be released by the designer after we have selected a final design.

Target Market(s)

Equestrian businesses

Industry/Entity Type

Business

Contact Information for Business Card

Gerard Vanhoorne
Title: zaakvoerder
Full Stable Works Vanhoorne GCV
Lindekouter 47
B - 9999 Voorbeeldegem
België
Phone: + 32 400 98 76 10
Mail: gerard@fswvanhoorne-example.eu

Font styles to use
Serif

Requirements
Must have
• My own logo
• See attached files
• Website: fswvanhoorne-example.eu

```html
<!DOCTYPE html>
<html lang="nl">
<head>
<meta charset="utf-8">
<title>Full Stable Works Vanhoorne – Business Card</title>
<link rel="stylesheet" href="https://fonts.googleapis.com/css2?family=Libre+Baskerville:wght@400;700&display=swap">
<style>
  :root {
    --ink: #111111;
    --paper: #f6f6f6;
    --paper-edge: #e2e2e2;
    --band: #0b0b0b;
    --band-text: #f4f4f4;
    --backdrop: #d9d6d1;
    --muted: #2a2a2a;
  }
  * { box-sizing: border-box; margin: 0; padding: 0; }
  html, body {
    width: 1200px; height: 780px; overflow: hidden;
    background: var(--backdrop);
    font-family: "Libre Baskerville", "Times New Roman", serif;
    color: var(--ink);
  }
  .canvas {
    position: relative; width: 1200px; height: 780px;
    display: flex; align-items: center; justify-content: center; gap: 40px;
  }
  .card {
    position: relative; width: 540px; height: 310px;
    background: linear-gradient(135deg, #ffffff 0%, var(--paper) 55%, var(--paper-edge) 100%);
    border-radius: 16px; overflow: hidden;
    box-shadow: 0 10px 26px rgba(0,0,0,0.25);
  }

  /* Front */
  .card-front .brand {
    position: absolute; top: 44px; left: 0; right: 0;
    display: flex; align-items: center; justify-content: center; gap: 12px;
  }
  .brand-dot {
    width: 30px; height: 30px; border-radius: 50%; background: var(--ink);
    flex: none;
  }
  .brand-name {
    font-weight: 700; font-size: 23px; letter-spacing: 0.5px; text-transform: uppercase;
  }
  .person {
    position: absolute; top: 112px; left: 0; right: 0; text-align: center;
  }
  .person-name { font-weight: 700; font-size: 17px; letter-spacing: 0.5px; }
  .person-title { font-size: 14px; margin-top: 4px; }
  .contact {
    position: absolute; top: 176px; left: 0; right: 0; text-align: center;
    font-size: 13px; line-height: 1.6; color: var(--muted);
  }
  .address-band {
    position: absolute; left: 0; right: 0; bottom: 0; height: 52px;
    background: var(--band); color: var(--band-text);
    display: flex; align-items: center; justify-content: center;
    font-size: 15px; letter-spacing: 0.3px;
  }

  /* Back */
  .card-back .mark {
    position: absolute; top: 50%; left: 58%; transform: translate(-50%, -50%);
    display: flex; flex-direction: column; align-items: center; gap: 14px;
  }
  .mark .brand-dot { width: 96px; height: 96px; }
  .mark .brand-name { font-size: 15px; text-align: center; }
  .website {
    position: absolute; top: 50%; left: 78px;
    transform: translate(-50%, -50%) rotate(90deg);
    font-size: 15px; font-weight: 700; white-space: nowrap;
  }
</style>
</head>
<body>
<main class="canvas">
  <section class="card card-front" aria-label="Front of business card">
    <div class="brand">
      <span class="brand-dot"></span>
      <span class="brand-name">Full Stable Works Vanhoorne</span>
    </div>
    <div class="person">
      <p class="person-name">EMPLOYEE NAME</p>
      <p class="person-title">Your Title</p>
    </div>
    <div class="contact">
      <p>+ 32 400 98 76 10</p>
      <p>gerard@fswvanhoorne-example.eu</p>
    </div>
    <div class="address-band">Lindekouter 47, B - 9999 Voorbeeldegem, België</div>
  </section>

  <section class="card card-back" aria-label="Back of business card">
    <p class="website">fswvanhoorne-example.eu</p>
    <div class="mark">
      <span class="brand-dot"></span>
      <span class="brand-name">Full Stable Works Vanhoorne</span>
    </div>
  </section>
</main>
</body>
</html>
```